flatrotate.co.uk landing page website design

Hi designers, I would like a custom designed landing page very similar to www.dwellingtrader.co.uk. It represents a happy place, sunny days and people swapping homes. I would like this done just like theres but our own design but a similar layout as theres.

I would like the 3 reasons to use us to be

Connect to thousands of other people in your area looking for a home swap

Our service is Completely free unlike most other exchange websites.

Find a exchange within 30 days!*

Thank you all,

Hi Everyone, I need the designs to represent london if possible like one of the designers has done for anyone else being in with a chance to win. Please check out the design by KR with the london look. I still like some of the others and they may win but i need to give this a try please.

Target Market(s)

Council house tenants

Coding

Coded - Design and coding required

Number of Pages Required

1 page

Requirements
Must have
• Custom designed landing page showing all the elements that www.dwellingtrader.co.uk use, The blue sky, and the land it shows with houses and people representing people swapping house. It can not be the same as them but can be similar concept with our own custom design and colour scheme ect.

please create 3 bubbles for speech from people. Please add the following quotes. "Its time we upsize"
"lets try and downsize and save money" "shall we move house?"
Would like 2 blocks of flats in a similar way dwelling trader.co.uk show the houses.
Nice to have

Should not have
• Same colour scheme as dwelling trader apart from the blue sky

```html
<!DOCTYPE html>
<html lang="en">
<head>
<meta charset="utf-8">
<title>flatrotate.co.uk – Council home exchange</title>
<link href="https://fonts.googleapis.com/css2?family=Montserrat:wght@400;500;600;700;800&display=swap" rel="stylesheet">
<style>
:root{
  --sky:#a0dff7;
  --ink:#1a1a1a;
  --navy:#1622a6;
  --green-dark:#0f5e0f;
  --green-mid:#2f9e3a;
  --green-bright:#53e07b;
  --green-text:#36b54a;
  --panel:#000000;
  --white:#ffffff;
  --muted:#a6a6a6;
  --footer-bg:#f7f8fa;
  --red:#ff2b2b;
}
*{box-sizing:border-box;margin:0;padding:0}
html,body{width:1200px;height:2770px;overflow:hidden}
body{position:relative;background:var(--sky);font-family:'Montserrat',sans-serif;color:var(--ink)}
.abs{position:absolute}

/* header */
.brand{left:115px;top:108px;display:flex;align-items:center;gap:14px}
.brand-square{width:56px;height:56px;background:var(--green-mid)}
.brand-name{font-size:46px;font-weight:600;color:var(--ink);letter-spacing:-0.5px}
.btn-register{left:760px;top:131px;width:153px;height:54px;background:var(--navy);color:#fff;border-radius:14px 0 0 14px;font-size:17px;font-weight:700;display:flex;align-items:center;justify-content:center}
.btn-login{left:925px;top:131px;width:154px;height:54px;background:var(--green-dark);color:#fff;border-radius:0 27px 27px 0;font-size:17px;font-weight:700;display:flex;align-items:center;justify-content:center}

.hero-title{left:0;top:286px;width:1214px;text-align:center;font-size:36px;font-weight:800;letter-spacing:.5px}

/* search panel */
.search{left:121px;top:361px;width:958px;height:391px;background:var(--panel)}
.search-label{color:#fff;font-size:21px;font-weight:700;position:absolute}
.search-field{position:absolute;background:#fff;border-radius:5px;height:60px;color:var(--muted);font-size:21px;font-weight:600;display:flex;align-items:center;padding-left:11px}
.caret{position:absolute;right:16px;top:30px;width:0;height:0;border-left:15px solid transparent;border-right:15px solid transparent;border-top:14px solid #555}
.search-btn{position:absolute;left:35px;top:260px;width:910px;height:60px;background:#fff;border-radius:5px;font-size:24px;font-weight:600;display:flex;align-items:center;justify-content:center;color:#222}

.tagline{left:0;top:776px;width:1200px;text-align:center;font-size:31px;font-weight:700;color:var(--green-mid)}
.tagline span{color:#3b3b3b}

.role-btn{top:911px;height:106px;width:367px;border-radius:44px 0 44px 0;display:flex;align-items:center;justify-content:center;text-align:center;font-size:21px;line-height:1.2;padding:0 8px}
.role-tenant{left:221px;background:var(--green-dark);color:#fff;border:5px solid #000}
.role-landlord{left:607px;background:#fff;color:#111;border:5px solid var(--green-dark);border-radius:0 44px 0 44px}

/* scene */
.scene{left:0;top:1040px;width:1200px;height:507px}
.bubble{position:absolute;font-size:19px;line-height:1.15;text-align:center;display:flex;align-items:center;justify-content:center;border-radius:50%}
.bubble-green{background:var(--green-dark);color:#fff;border:4px solid var(--sky)}
.bubble-orange{background:#b5620e;color:#fff;border:4px solid var(--sky)}

/* why section */
.why{left:0;top:1547px;width:1200px;height:629px;background:var(--green-bright)}
.why-title{left:0;top:1590px;width:1200px;text-align:center;font-size:31px;font-weight:800}
.why-sub{left:0;top:1662px;width:1184px;text-align:center;font-size:24px;font-weight:500}
.card-days{left:227px;top:1745px;width:193px;height:219px}
.card-days .shape{position:absolute;left:10px;top:0;width:180px;height:140px;background:var(--green-mid)}
.card-days .label{position:absolute;left:0;top:118px;width:193px;height:101px;border:3px solid #000;border-top:none;background:var(--green-bright);text-align:center;font-size:19px;font-weight:700;line-height:1.15;padding-top:14px}
.card-days .label b{display:block;color:var(--red);font-size:32px;font-weight:800;margin-top:4px}
.card-connect{left:565px;top:1783px;width:446px;height:140px;background:var(--green-dark);border:3px solid #000;border-radius:10px;display:flex;align-items:center}
.card-connect .icon{width:106px;height:136px;background:var(--green-bright);border-radius:8px 0 0 8px;border-right:3px solid #000}
.card-connect p{flex:1;color:#fff;font-weight:700;font-size:21px;text-align:center;line-height:1.22}
.card-connect p span{color:var(--red)}
.nav-arrow{top:1808px}

.treeline{left:0;top:2025px;width:1200px;height:151px}

/* footer */
.footer{left:0;top:2176px;width:1200px;height:594px;background:var(--footer-bg)}
.f-head{font-size:22px;font-weight:500;color:var(--green-text);line-height:1.55}
.f-links{list-style:none;font-size:19px;line-height:44px;color:#222}
.f-item{display:flex;align-items:center;gap:20px;font-size:19px;color:#222}
.dot{width:30px;height:30px;border-radius:50%}
.legal{top:2726px;font-size:19px;color:#222}
</style>
</head>
<body>

<header>
  <div class="abs brand"><span class="brand-square"></span><span class="brand-name">flatrotate.co.uk</span></div>
  <div class="abs btn-register">REGISTER</div>
  <div class="abs btn-login">LOG IN</div>
</header>

<h1 class="abs hero-title">YOUR DREAM HOME IS A MOMENT AWAY</h1>

<section class="abs search">
  <span class="search-label" style="left:35px;top:42px">LOCATION</span>
  <span class="search-label" style="left:433px;top:42px">BEDROOMS</span>
  <span class="search-label" style="left:654px;top:38px">MAX. RENT ($ PER MONTH)</span>
  <div class="search-field" style="left:19px;top:79px;width:357px">Town or Postcode</div>
  <div class="search-field" style="left:432px;top:79px;width:195px">Any<span class="caret"></span></div>
  <div class="search-field" style="left:666px;top:79px;width:277px">Any<span class="caret"></span></div>
  <div class="search-btn">SEARCH</div>
</section>

<p class="abs tagline">We are changing the way people exchange <span>council homes</span></p>

<div class="abs role-btn role-tenant"><span><b>Are you a tenant?</b> Click here<br>for more information</span></div>
<div class="abs role-btn role-landlord"><span><b>Are you a landlord?</b> Click here<br>for more information</span></div>

<section class="abs scene">
  <div role="img" aria-label="Sunny illustrated landscape with two blocks of flats, a house, trees, a road and families thinking about swapping homes" style="position:absolute;inset:0;background:linear-gradient(to bottom,var(--sky) 0%,var(--sky) 24%,#3f7a32 30%,#2e6b28 65%,#1f5a1f 100%)"></div>
  <div class="bubble bubble-green" style="left:101px;top:204px;width:140px;height:88px">Its time we<br>upsize</div>
  <div class="bubble bubble-green" style="left:538px;top:210px;width:148px;height:86px">shall we move<br>house?</div>
  <div class="bubble bubble-orange" style="left:1006px;top:156px;width:172px;height:118px">lets try and<br>downsize and<br>save money</div>
</section>

<section class="abs why"></section>
<h2 class="abs why-title">WHY CHOOSE FLATROTATE</h2>
<p class="abs why-sub">WE CONNECT YOU TO HUNDREDS OF THOUSANDS OF OTHER PEOPLE LOOK</p>

<svg class="abs nav-arrow" style="left:28px" width="68" height="92" viewBox="0 0 68 92"><polyline points="60,6 10,46 60,86" fill="none" stroke="var(--green-dark)" stroke-width="9"/></svg>
<svg class="abs nav-arrow" style="left:1094px" width="68" height="92" viewBox="0 0 68 92"><polyline points="8,6 58,46 8,86" fill="none" stroke="var(--green-dark)" stroke-width="9"/></svg>

<div class="abs card-days">
  <div class="shape"></div>
  <div class="label">Find a exchange<br>within<b>30 days!</b></div>
</div>

<div class="abs card-connect">
  <svg class="icon" viewBox="0 0 106 136">
    <g stroke="#000" stroke-width="3">
      <line x1="55" y1="72" x2="20" y2="30"/><line x1="55" y1="72" x2="88" y2="40"/>
      <line x1="55" y1="72" x2="18" y2="86"/><line x1="55" y1="72" x2="24" y2="118"/>
      <line x1="55" y1="72" x2="80" y2="118"/>
    </g>
    <g fill="#000">
      <circle cx="55" cy="72" r="11"/><circle cx="20" cy="30" r="7"/><circle cx="88" cy="40" r="7"/>
      <circle cx="18" cy="86" r="7"/><circle cx="24" cy="118" r="7"/><circle cx="80" cy="118" r="7"/>
    </g>
  </svg>
  <p>Connect to thousands of<br>other<br>people in your area looking<br>for a <span>HOME SWAP</span></p>
</div>

<div class="abs treeline" role="img" aria-label="White silhouette of trees, houses and London-style buildings along the skyline" style="background:linear-gradient(to bottom,var(--green-bright) 0%,#cfeedb 55%,var(--footer-bg) 100%)"></div>

<footer class="abs footer"></footer>
<div class="abs" style="left:150px;top:2290px">
  <h3 class="f-head">QUICK LINKS</h3>
  <ul class="f-links" style="margin-top:6px">
    <li>Contact Us</li><li>About Us</li><li>Terms of Use</li><li>Privacy</li>
    <li>Accessibility</li><li>Cookies</li><li>Ad privacy</li><li>Help</li>
  </ul>
</div>
<div class="abs" style="left:397px;top:2290px;width:300px">
  <h3 class="f-head">HOUSE SWAP ADVICE<br>AND TIPS</h3>
  <div class="f-item" style="margin:4px 0 0 0"><span class="dot" style="background:#a9a9c8"></span>Blog</div>
  <h3 class="f-head" style="margin-top:22px">CONNECT WITH US</h3>
  <div class="f-item" style="margin-top:8px"><span class="dot" style="background:#3b5bd6;width:16px;height:28px;border-radius:0"></span><span style="margin-left:14px">Friendnet</span></div>
</div>
<div class="abs" style="left:734px;top:2290px;width:420px">
  <h3 class="f-head">CONTACT INFO</h3>
  <div class="f-item" style="margin:12px 0 0 -14px">
    <svg width="40" height="40" viewBox="0 0 40 40"><circle cx="20" cy="20" r="18" fill="#e4f2fb" stroke="#2d8bd6" stroke-width="3"/><path d="M13 11c2-1 4 3 5 5s-2 2-1 4 3 4 4 4 2-3 4-1 4 3 2 5-6 1-9-2-7-8-5-15z" fill="#2d8bd6"/></svg>
    020 7946 0382</div>
  <div class="f-item" style="margin:18px 0 0 -14px">
    <svg width="40" height="34" viewBox="0 0 40 34"><rect x="2" y="6" width="36" height="26" fill="#4aa3e8"/><polyline points="2,6 20,20 38,6" fill="none" stroke="#fff" stroke-width="3"/></svg>
    info@flatrotate.co.uk</div>
</div>

<p class="abs legal" style="left:35px">Copyright © 2020 Flatrotate - All Rights Reserved.</p>
<p class="abs legal" style="right:27px">Powered by MN Studio</p>

</body>
</html>
```